Calloway Holdings Website Design

We are a private equity firm based with offices based in Hong Kong, Singapore, London and Paris. Our focus is investments in property development projects, corporate ventures and loans.

We require the development of a new website and you will have to select relevant images from the likes of PixBarrel or other stock photo libraries.

We will need a design done for a PC based website and the designer selected with the favored design will also need to produce some concepts for a responsive website.

Target Market(s)

Sophisticated investors looking to invest in high return property development, businesses and mortgages.

Industry/Entity Type

Investment

Number of Pages Required

5+ page

Font styles to use
Serif
Sans Serif

Colors
0255a3
00a990

Requirements
Must have
• Clean modern feel and must portray stability and professionalism.

```html
<!DOCTYPE html>
<html lang="en">
<head>
<meta charset="utf-8">
<title>Calloway Holdings</title>
<link rel="stylesheet" href="https://fonts.googleapis.com/css2?family=Exo+2:wght@500;600;700&family=Open+Sans:wght@400;600;700&family=Roboto:wght@400;500;700&display=swap">
<style>
:root{
  --blue:#0255a3;
  --blue-deep:#013f7a;
  --teal:#00a990;
  --ink:#111111;
  --text:#333333;
  --light:#f5f5f5;
  --footer:#232323;
  --footer-deep:#121212;
  --footer-text:#f1c96a;
  --link:#3aa0d8;
  --price:#00c9a7;
}
*{box-sizing:border-box;margin:0;padding:0}
html,body{width:1200px;height:2769px;overflow:hidden}
body{font-family:"Open Sans",Arial,sans-serif;color:var(--text);background:#fff;position:relative}
.abs{position:absolute}

/* top bar */
.topbar{left:0;top:0;width:1200px;height:44px;background:var(--blue-deep);color:#fff;font:500 12px "Roboto",sans-serif}
.topbar .welcome{left:64px;top:15px;letter-spacing:.5px}
.topbar .links{right:64px;top:14px;display:flex;gap:26px}
.topbar .links span{display:flex;align-items:center;gap:6px}
.topbar .links svg{flex:none}

/* header */
.header{left:0;top:44px;width:1200px;height:108px;background:#fff}
.brand{left:70px;top:36px;display:flex;align-items:center;gap:12px;font:700 26px "Exo 2",sans-serif;color:var(--blue-deep);letter-spacing:.5px}
.brand .dot{width:28px;height:28px;border-radius:50%;background:var(--teal)}
.nav{right:62px;top:38px;display:flex;font:500 13px "Roboto",sans-serif;color:var(--ink)}
.nav span{padding:9px 13px;margin-left:10px;border:2px solid transparent}
.nav .active{border-color:var(--blue)}

/* hero */
.hero{left:0;top:152px;width:1200px;height:546px;background:linear-gradient(180deg,#3d4456 0%,#b87a55 26%,#495363 46%,#2d3a4d 70%,#1c2433 100%)}
.hero-title{left:61px;top:255px;width:497px;height:87px;background:var(--teal);color:#fff;font:600 31px "Exo 2",sans-serif;letter-spacing:2px;padding:24px 0 0 47px}

/* section titles */
.sec-title{left:0;width:1200px;text-align:center;font:700 32px "Exo 2",sans-serif;color:var(--ink);letter-spacing:1px}
.rule{left:565px;width:70px;height:4px;background:var(--teal)}
.intro{left:88px;top:822px;width:1024px;text-align:center;font-size:13.5px;line-height:25px;color:#222}

/* service cards */
.arrow{top:1042px}
.card{top:932px;width:251px;height:310px;overflow:hidden}
.card .photo{position:absolute;inset:0}
.card .icon{position:absolute;left:0;top:0;width:70px;height:58px;background:var(--blue);display:flex;align-items:center;justify-content:center}
.card .label{position:absolute;left:0;top:231px;width:251px;height:37px;background:var(--blue);color:#fff;font:500 13.5px "Roboto",sans-serif;padding:11px 0 0 4px;clip-path:polygon(0 0,100% 0,82% 100%,0 100%)}
.card.lead .panel{position:absolute;left:0;top:0;width:251px;height:232px;background:var(--teal);color:#fff;padding:66px 20px 0 28px;font-size:13.5px;line-height:24px}
.card.lead .panel b{display:block;margin-top:18px;font-weight:700}
.card.lead .sub{position:absolute;left:0;top:240px;font:500 13px "Roboto",sans-serif;color:#333}
.card.lead .foot{position:absolute;left:0;top:272px;width:251px;height:38px;background:var(--teal);clip-path:polygon(0 0,82% 0,62% 100%,0 100%)}

/* testimonials */
.quotes{left:0;top:1242px;width:1200px;height:623px;background:var(--light)}
.quote{left:130px;top:1508px;width:940px;text-align:center;font-size:13.5px;line-height:23px;color:#222}
.q-name{left:0;top:1627px;width:1200px;text-align:center;font:700 14px "Roboto",sans-serif;letter-spacing:2px;color:#222}
.q-place{left:0;top:1649px;width:1200px;text-align:center;font-size:13px;color:#444}
.thumb{top:1717px;width:82px;height:83px}
.thumb.on{border:2px solid #555;padding:5px;background:#fff}
.thumb .ph{width:100%;height:100%}

/* agents */
.agent{top:2014px;width:247px}
.agent .ph{width:192px;height:249px}
.agent .social{position:absolute;left:192px;top:0;width:55px;height:249px;background:var(--blue);display:flex;flex-direction:column;align-items:center;padding-top:10px;gap:13px}
.agent .social span{width:34px;height:34px;border:2px solid #fff;border-radius:50%;display:flex;align-items:center;justify-content:center}
.agent .name{display:flex;justify-content:space-between;align-items:center;padding:16px 16px 0 20px;font-size:14.5px;color:#222}

/* footer */
.footer{left:0;top:2311px;width:1200px;height:403px;background:var(--footer)}
.skyline{left:0;top:2598px;width:1200px;height:116px;background:linear-gradient(180deg,rgba(20,20,20,0) 0%,#0b0b0b 80%)}
.f-col{top:2342px}
.f-col h4{font:700 17px "Roboto",sans-serif;color:#fff;letter-spacing:.3px}
.f-col .bar{width:36px;height:3px;background:var(--teal);margin:10px 0 22px}
.f-about p{color:var(--footer-text);font-size:13px;line-height:26px;width:230px}
.f-social{display:flex;gap:14px;margin-top:30px}
.f-social span{width:30px;height:30px;border:1px solid #555;display:flex;align-items:center;justify-content:center}
.tweet{display:flex;gap:14px;color:var(--footer-text);font-size:12.5px;line-height:25px;margin-bottom:20px;width:250px}
.tweet svg{flex:none;margin-top:5px}
.tweet a{color:var(--link);text-decoration:none}
.prop{display:flex;gap:16px;margin-bottom:26px}
.prop .ph{width:56px;height:46px;flex:none}
.prop .t{font-size:11px;line-height:20px;color:#fff;width:150px}
.prop .p{color:var(--price);font-size:13px}
.contact li{list-style:none;display:flex;gap:16px;color:#fff;font-size:13px;line-height:21px;margin-bottom:19px}
.contact svg{flex:none;margin-top:4px}
.bottom{left:0;top:2714px;width:1200px;height:55px;background:var(--footer-deep);color:#fff;font:700 10.5px "Roboto",sans-serif;padding:22px 0 0 79px;letter-spacing:.5px}
</style>
</head>
<body>

<div class="abs topbar">
  <div class="abs welcome">WELCOME VISITOR</div>
  <div class="abs links">
    <span><svg width="12" height="12" viewBox="0 0 12 12"><circle cx="6" cy="6" r="5" fill="none" stroke="#c8d6ea" stroke-width="1.4"/><path d="M1 6h10M6 1c-2 3-2 7 0 10M6 1c2 3 2 7 0 10" fill="none" stroke="#c8d6ea" stroke-width="1"/></svg>Language</span>
    <span><svg width="12" height="12" viewBox="0 0 12 12"><path d="M2 10l7-7M7 2h3v3" fill="none" stroke="#c8d6ea" stroke-width="1.6"/></svg>Login</span>
    <span><svg width="12" height="12" viewBox="0 0 12 12"><circle cx="6" cy="4" r="2.6" fill="#c8d6ea"/><path d="M1 12c0-3 2.5-4.5 5-4.5S11 9 11 12z" fill="#c8d6ea"/></svg>Membership</span>
    <span><svg width="8" height="12" viewBox="0 0 8 12"><path d="M7 3C6 1.5 1 1.5 1 3.5S7 5.5 7 8 2 10.5 1 9M4 0v12" fill="none" stroke="#c8d6ea" stroke-width="1.3"/></svg>Currency</span>
  </div>
</div>

<header class="abs header">
  <div class="abs brand"><span class="dot"></span>Calloway Holdings</div>
  <nav class="abs nav"><span class="active">HOME</span><span>ABOUT</span><span>SERVICES</span><span>INVESTMENT APPROACH</span><span>MISSIONS AND VALUES</span><span>CONTACT</span></nav>
</header>

<div class="abs hero" role="img" aria-label="Dusk skyline photo of a dense city with a tall spire tower at centre"></div>
<div class="abs hero-title">CALLOWAY HOLDINGS</div>

<h2 class="abs sec-title" style="top:738px">SERVICES WE PROVIDE</h2>
<div class="abs rule" style="top:788px"></div>
<p class="abs intro">This time there is no stopping us. Straightnin the curves. Flatnin' the hills Someday the mountain might get 'em but the law never will. The weather started getting rough - the tiny ship was tossed.his time there is no stopping us. Straightnin the curves. Flatnin' the hills Someday the mountain might get 'em but the law never will. The weather started getting rough - the tiny ship was tossed.</p>

<svg class="abs arrow" style="left:16px" width="18" height="28" viewBox="0 0 18 28"><path d="M14 3 4 14l10 11" fill="none" stroke="#111" stroke-width="4"/></svg>
<svg class="abs arrow" style="left:1166px" width="18" height="28" viewBox="0 0 18 28"><path d="M4 3l10 11L4 25" fill="none" stroke="#111" stroke-width="4"/></svg>

<div class="abs card lead" style="left:61px">
  <div class="panel">And when the odds are against him and their dangers work to do. You bet your life Swift Rider<b>Read more</b></div>
  <svg class="abs" style="left:10px;top:10px" width="36" height="34" viewBox="0 0 36 34"><rect x="5" y="8" width="26" height="18" fill="none" stroke="#fff" stroke-width="2" transform="rotate(-20 18 17)"/><circle cx="18" cy="17" r="4" fill="none" stroke="#fff" stroke-width="2"/></svg>
  <div class="sub">OUR OWN FUNDS</div>
  <div class="foot"></div>
</div>

<div class="abs card" style="left:334px">
  <div class="photo" role="img" aria-label="Photo of business people meeting in a bright office" style="background:linear-gradient(160deg,#f2f2f2,#c9cbd3 55%,#e4e6ea)"></div>
  <div class="icon"><svg width="34" height="30" viewBox="0 0 34 30"><path d="M4 14 17 3l13 11M8 12v14h18V12" fill="none" stroke="#fff" stroke-width="2.4"/></svg></div>
  <div class="label">INSTITUTIONAL INVESTORS</div>
</div>

<div class="abs card" style="left:613px">
  <div class="photo" role="img" aria-label="Photo of a modern dark house lit warmly at dusk" style="background:linear-gradient(180deg,#5c6f9a 0%,#2c2f3f 45%,#6a5446 80%,#8b8a86)"></div>
  <div class="icon"><svg width="26" height="32" viewBox="0 0 26 32"><rect x="4" y="3" width="18" height="27" fill="none" stroke="#fff" stroke-width="2.4"/><path d="M9 9h2M15 9h2M9 15h2M15 15h2M9 21h2M15 21h2" stroke="#fff" stroke-width="2.4"/></svg></div>
  <div class="label">ADVISORS AND CONSULTANTS</div>
</div>

<div class="abs card" style="left:888px">
  <div class="photo" role="img" aria-label="Photo of a factory floor with green machinery" style="background:linear-gradient(180deg,#d8e0e4 0%,#9cb0b8 45%,#7fa86a 70%,#6d8fa8)"></div>
  <div class="icon"><svg width="30" height="30" viewBox="0 0 30 30"><path d="M3 14 15 3l12 11v13H3z" fill="#fff"/><rect x="12" y="18" width="6" height="9" fill="#0255a3"/></svg></div>
  <div class="label">CORPORATE INVESTORS</div>
</div>

<div class="abs quotes"></div>
<h2 class="abs sec-title" style="top:1344px">SOME WORDS FROM OUR CUSTOMER</h2>
<div class="abs rule" style="top:1393px"></div>
<svg class="abs" style="left:579px;top:1455px" width="40" height="36" viewBox="0 0 40 36"><path d="M3 3h34v23H18l-8 7v-7H3z" fill="none" stroke="#333" stroke-width="2"/><circle cx="13" cy="14" r="2" fill="#333"/><circle cx="20" cy="14" r="2" fill="#333"/><circle cx="27" cy="14" r="2" fill="#333"/></svg>
<p class="abs quote">Can you tell me how to get how to get to Maple Lane. Believe it or not I'm walking on air. I never thought I could feel so free. The movie star the professor and Mary Ann here on Harbor Isle. Just two good ol' boys<br>LENA WARD Sydney, Australia</p>
<div class="abs q-name">LENA WARD</div>
<div class="abs q-place">Australia</div>
<div class="abs thumb on" style="left:462px"><div class="ph" role="img" aria-label="Portrait of a smiling customer in yellow" style="background:linear-gradient(180deg,#d8d8d8,#e8c23a)"></div></div>
<div class="abs thumb" style="left:556px"><div class="ph" role="img" aria-label="Portrait of a male customer" style="background:linear-gradient(180deg,#d6d6d6,#6d8fb8)"></div></div>
<div class="abs thumb" style="left:644px"><div class="ph" role="img" aria-label="Portrait of a male customer in blue" style="background:linear-gradient(180deg,#dcdcdc,#3a84c6)"></div></div>

<h2 class="abs sec-title" style="top:1876px">OUR GREAT AGENTS</h2>
<div class="abs rule" style="top:1925px"></div>

<svg width="0" height="0" style="position:absolute">
  <defs>
    <g id="i-share"><circle cx="4" cy="8" r="2.2" fill="#fff"/><circle cx="12" cy="3.5" r="2.2" fill="#fff"/><circle cx="12" cy="12.5" r="2.2" fill="#fff"/><path d="M4 8l8-4.5M4 8l8 4.5" stroke="#fff" stroke-width="1.4"/></g>
    <g id="i-plus"><path d="M8 2v12M2 8h12" stroke="#fff" stroke-width="2.2"/></g>
    <g id="i-link"><rect x="1" y="5" width="8" height="6" rx="3" fill="none" stroke="#fff" stroke-width="1.6"/><rect x="7" y="5" width="8" height="6" rx="3" fill="none" stroke="#fff" stroke-width="1.6"/></g>
    <g id="i-globe"><circle cx="8" cy="8" r="6.2" fill="none" stroke="#fff" stroke-width="1.5"/><path d="M2 8h12M8 2c-3 4-3 8 0 12M8 2c3 4 3 8 0 12" fill="none" stroke="#fff" stroke-width="1.1"/></g>
    <g id="i-mail"><rect x="1.5" y="3.5" width="13" height="9" fill="none" stroke="#fff" stroke-width="1.5"/><path d="M2 4l6 5 6-5" fill="none" stroke="#fff" stroke-width="1.5"/></g>
    <g id="i-phone"><rect width="14" height="14" rx="2" fill="#333"/><path d="M4 3c-1 1 0 5 3 7s4 1 4 0l-2-2-1 1C6 8 5 7 5 6l1-1z" fill="#fff"/></g>
  </defs>
</svg>

<div class="abs agent" style="left:61px">
  <div class="ph" role="img" aria-label="Photo of an agent in a suit outside a house" style="background:linear-gradient(180deg,#8fb8e6,#6f9a4e 70%,#5d7b3c)"></div>
  <div class="social"><span><svg width="16" height="16"><use href="#i-share"/></svg></span><span><svg width="16" height="16"><use href="#i-plus"/></svg></span><span><svg width="16" height="16"><use href="#i-link"/></svg></span><span><svg width="16" height="16"><use href="#i-globe"/></svg></span><span><svg width="16" height="16"><use href="#i-mail"/></svg></span></div>
  <div class="name">Marcus Hale<svg width="14" height="14"><use href="#i-phone"/></svg></div>
</div>
<div class="abs agent" style="left:339px">
  <div class="ph" role="img" aria-label="Portrait of a smiling agent with yellow tie" style="background:linear-gradient(180deg,#f4f4f4,#e6e6e6 50%,#2a2e3a)"></div>
  <div class="social"><span><svg width="16" height="16"><use href="#i-share"/></svg></span><span><svg width="16" height="16"><use href="#i-plus"/></svg></span><span><svg width="16" height="16"><use href="#i-link"/></svg></span><span><svg width="16" height="16"><use href="#i-globe"/></svg></span><span><svg width="16" height="16"><use href="#i-mail"/></svg></span></div>
  <div class="name">Owen Pratt<svg width="14" height="14"><use href="#i-phone"/></svg></div>
</div>
<div class="abs agent" style="left:605px">
  <div class="ph" role="img" aria-label="Portrait of an agent in a dark shirt" style="background:linear-gradient(180deg,#ededed,#dadada 50%,#1e1e22)"></div>
  <div class="social"><span><svg width="16" height="16"><use href="#i-share"/></svg></span><span><svg width="16" height="16"><use href="#i-plus"/></svg></span><span><svg width="16" height="16"><use href="#i-link"/></svg></span><span><svg width="16" height="16"><use href="#i-globe"/></svg></span><span><svg width="16" height="16"><use href="#i-mail"/></svg></span></div>
  <div class="name">Marcus Hale<svg width="14" height="14"><use href="#i-phone"/></svg></div>
</div>
<div class="abs agent" style="left:889px">
  <div class="ph" role="img" aria-label="Portrait of an agent in a dark suit" style="background:linear-gradient(180deg,#2a2a2a,#4a4440 50%,#161616)"></div>
  <div class="social"><span><svg width="16" height="16"><use href="#i-share"/></svg></span><span><svg width="16" height="16"><use href="#i-plus"/></svg></span><span><svg width="16" height="16"><use href="#i-link"/></svg></span><span><svg width="16" height="16"><use href="#i-globe"/></svg></span><span><svg width="16" height="16"><use href="#i-mail"/></svg></span></div>
  <div class="name">Owen Pratt<svg width="14" height="14"><use href="#i-phone"/></svg></div>
</div>

<footer>
  <div class="abs footer"></div>
  <div class="abs skyline" role="img" aria-label="Dark city skyline silhouette along the footer base"></div>

  <div class="abs f-col f-about" style="left:79px">
    <h4>ABOUT US</h4><div class="bar"></div>
    <p>You wanna be where you can see our troubles are all the same. You wanna be where everybody knows Your name. Here's the story of a their tropic island nest.</p>
    <div class="f-social"><span><svg width="14" height="14" viewBox="0 0 16 16"><use href="#i-share"/></svg></span><span><svg width="14" height="14" viewBox="0 0 16 16"><use href="#i-plus"/></svg></span><span><svg width="14" height="14" viewBox="0 0 16 16"><use href="#i-link"/></svg></span><span><svg width="14" height="14" viewBox="0 0 16 16"><use href="#i-globe"/></svg></span></div>
  </div>

  <div class="abs f-col" style="left:348px">
    <h4>RECENT TWEETS</h4><div class="bar"></div>
    <div class="tweet"><svg width="16" height="14" viewBox="0 0 16 14"><path d="M1 2h14v8H7l-4 3v-3H1z" fill="#777"/></svg><div>RT @lenorefield: PressKit Is Revamping Its Testimonials Page with #iloveevp Social Media Campaign <a>https://lnk.to/81yNRtXAca</a> <a>about 8 hours ago</a></div></div>
    <div class="tweet"><svg width="16" height="14" viewBox="0 0 16 14"><path d="M1 2h14v8H7l-4 3v-3H1z" fill="#777"/></svg><div>Contributor Weekend: Support Forums <a>https://lnk.to/vdIjPOTkF5</a> <a>about 12 hours ago</a></div></div>
  </div>

  <div class="abs f-col" style="left:618px">
    <h4>RECENT PROPERTIES</h4><div class="bar"></div>
    <div class="prop"><div class="ph" role="img" aria-label="Small photo of a modern house" style="background:linear-gradient(180deg,#9cc3e6,#6f8a5a)"></div><div class="t">SWEET HOME FOR SMALL FAMILY6<div class="p">$ 2,956,596</div></div></div>
    <div class="prop"><div class="ph" role="img" aria-label="Small photo of a family house" style="background:linear-gradient(180deg,#b6d2ea,#7c8f6a)"></div><div class="t">SWEET HOME FOR SMALL FAMILY5<div class="p">$ 256,596</div></div></div>
    <div class="prop"><div class="ph" role="img" aria-label="Small photo of a white house" style="background:linear-gradient(180deg,#c4dcf0,#e8e8e8 50%,#6b8a4c)"></div><div class="t">SWEET HOME FOR SMALL FAMILY4<div class="p">$ 2,956,596</div></div></div>
  </div>

  <div class="abs f-col contact" style="left:888px">
    <h4>CONTACT</h4><div class="bar"></div>
    <ul>
      <li><svg width="10" height="14" viewBox="0 0 10 14"><path d="M5 0a5 5 0 0 1 5 5c0 4-5 9-5 9S0 9 0 5a5 5 0 0 1 5-5z" fill="#fff"/><circle cx="5" cy="5" r="2" fill="#232323"/></svg><span>14 HARBOUR ROW, CENTRAL,<br>HONG KONG</span></li>
      <li><svg width="12" height="12" viewBox="0 0 14 14"><path d="M3 1c-2 2 0 7 3 9s6 3 7 1l-3-3-2 1C6 8 5 7 5 6l1-2z" fill="#fff"/></svg><span>+01 555 010 24</span></li>
      <li><svg width="13" height="12" viewBox="0 0 13 12"><rect x="3" y="0" width="7" height="3" fill="#fff"/><rect x="0" y="4" width="13" height="5" fill="#fff"/><rect x="3" y="8" width="7" height="4" fill="#fff"/></svg><span>+01 555 010 25</span></li>
      <li><svg width="13" height="10" viewBox="0 0 13 10"><rect x=".5" y=".5" width="12" height="9" fill="none" stroke="#fff"/><path d="M1 1l5.5 5L12 1" fill="none" stroke="#fff"/></svg><span>INFO@CALLOWAYHOLD.COM</span></li>
    </ul>
  </div>

  <div class="abs bottom">© CALLOWAY HOLDINGS &nbsp;ALL RIGHTS RESERVED</div>
</footer>

</body>
</html>
```